Business Card Design for Technology Company

New business card design needed for technology company director.
Ideally, the design will fit the style and nature of the industry. We are a supplier of quality products and services, and we hope the design will give customers and suppliers this impression.

Target Market(s)

3D Printing Industry

Industry/Entity Type

Technology Equipment

Contact Information for Business Card

Name: Henry Vo
Title: Director
Company address: Factory K4, 7B Lorimer Road, Springvale Victoria Australia 3150
Telephone: +61-3-8555 4613
Email: henry.vo@ferrolabs.com.au
Website: www.ferrolabs.com.au

Requirements
Must have
• All information in business card details
• Company logo
• '3D Printers and 3D Print Filaments' at proper place
Nice to have
• Style to fit the industry
• Colour to fit logo

```html
<!DOCTYPE html>
<html lang="en">
<head>
<meta charset="utf-8">
<title>Ferro Labs – Business Card</title>
<link href="https://fonts.googleapis.com/css2?family=Montserrat:wght@400;500;600;700&display=swap" rel="stylesheet">
<style>
  :root {
    --page-bg: #e9eaec;
    --card-white: #ffffff;
    --brand-blue: #1d4f8c;
    --brand-blue-deep: #123463;
    --brand-blue-light: #2f6fb6;
    --accent-orange: #f08a1c;
    --accent-yellow: #f7c21e;
    --stripe-grey: #b9bec6;
    --text-dark: #2a2f38;
    --text-light: #ffffff;
  }
  * { box-sizing: border-box; margin: 0; padding: 0; }
  html, body {
    width: 1200px; height: 870px; overflow: hidden;
    background: var(--page-bg);
    font-family: "Montserrat", sans-serif;
  }
  .stage { position: relative; width: 1200px; height: 870px; }
  .card {
    position: absolute; top: 280px;
    width: 540px; height: 310px;
    border-radius: 18px; overflow: hidden;
    box-shadow: 0 6px 20px rgba(0,0,0,0.18);
  }
  .card--front { left: 45px; background: var(--card-white); }
  .card--back {
    left: 615px;
    background: radial-gradient(circle at 50% 42%, var(--brand-blue-light) 0%, var(--brand-blue) 45%, var(--brand-blue-deep) 100%);
  }
  .front-wave { position: absolute; inset: 0; width: 100%; height: 100%; }

  .holder { position: absolute; left: 34px; top: 36px; }
  .holder__name {
    font-weight: 700; font-size: 19px; letter-spacing: 1px;
    color: var(--brand-blue); text-transform: uppercase;
  }
  .holder__title { font-size: 11px; color: var(--text-dark); margin-top: 4px; }

  .brand { display: flex; flex-direction: column; align-items: center; white-space: nowrap; }
  .brand__mark { background: var(--accent-orange); border-radius: 3px; }
  .brand__name { font-weight: 600; letter-spacing: 5px; text-transform: uppercase; }
  .brand__tagline { font-weight: 500; letter-spacing: 0.5px; }

  .card--front .brand { position: absolute; right: 34px; top: 34px; align-items: flex-end; }
  .card--front .brand__mark { width: 34px; height: 34px; margin-bottom: 10px; margin-right: 40px; }
  .card--front .brand__name { color: var(--text-dark); font-size: 24px; }
  .card--front .brand__tagline { color: var(--text-dark); font-size: 10px; margin-top: 4px; }

  .contacts {
    position: absolute; left: 34px; bottom: 30px;
    list-style: none; color: var(--text-light); font-size: 11.5px;
  }
  .contacts li { display: flex; align-items: center; gap: 9px; line-height: 20px; white-space: nowrap; }
  .contacts .icon {
    width: 13px; height: 13px; border-radius: 50%;
    background: var(--accent-orange); flex: none;
    display: flex; align-items: center; justify-content: center;
  }
  .address {
    position: absolute; right: 34px; bottom: 32px;
    color: var(--text-light); font-size: 12px; text-align: right; line-height: 20px; white-space: nowrap;
  }

  .card--back .brand { position: absolute; left: 50%; top: 50%; transform: translate(-50%, -50%); }
  .card--back .brand__mark { width: 46px; height: 46px; margin-bottom: 16px; }
  .card--back .brand__name { color: var(--text-light); font-size: 30px; }
  .card--back .brand__tagline { color: var(--text-light); font-size: 11px; margin-top: 8px; }
</style>
</head>
<body>
<main class="stage">

  <section class="card card--front" aria-label="Business card front">
    <svg class="front-wave" viewBox="0 0 540 310" preserveAspectRatio="none" aria-hidden="true">
      <path d="M0,150 C140,132 300,188 540,142 L540,166 C300,212 140,156 0,174 Z" fill="var(--stripe-grey)"/>
      <path d="M0,168 C140,150 300,206 540,160 L540,168 C300,214 140,158 0,176 Z" fill="var(--accent-orange)"/>
      <path d="M0,176 C140,158 300,214 540,168 L540,172 C300,218 140,162 0,180 Z" fill="var(--accent-yellow)"/>
      <path d="M0,184 C140,166 300,222 540,176 L540,310 L0,310 Z" fill="var(--brand-blue)"/>
    </svg>

    <div class="holder">
      <p class="holder__name">Henry Vo</p>
      <p class="holder__title">Director</p>
    </div>

    <div class="brand">
      <span class="brand__mark"></span>
      <span class="brand__name">Ferro Labs</span>
      <span class="brand__tagline">3D Printers and 3D Print Filaments</span>
    </div>

    <ul class="contacts">
      <li><span class="icon"><svg width="8" height="8" viewBox="0 0 10 10"><path d="M2 1 L4 1 L5 3 L4 4 Q5 6 6 6 L7 5 L9 6 L9 8 Q5 9 2 5 Q1 3 2 1Z" fill="#fff"/></svg></span>+61-3-8555 4613</li>
      <li><span class="icon"><svg width="8" height="8" viewBox="0 0 10 10"><rect x="1" y="2" width="8" height="6" rx="1" fill="#fff"/></svg></span>03 8555 4613</li>
      <li><span class="icon"><svg width="8" height="8" viewBox="0 0 10 10"><rect x="1" y="2" width="8" height="6" fill="none" stroke="#fff"/><path d="M1 2 L5 6 L9 2" fill="none" stroke="#fff"/></svg></span>henry.vo@ferrolabs.com.au</li>
      <li><span class="icon"><svg width="8" height="8" viewBox="0 0 10 10"><circle cx="5" cy="5" r="4" fill="none" stroke="#fff"/><path d="M1 5 H9 M5 1 V9" stroke="#fff"/></svg></span>www.ferrolabs.com.au</li>
    </ul>

    <p class="address">Factory K4, 7B Lorimer Road<br>Springvale Victoria Australia 3150</p>
  </section>

  <section class="card card--back" aria-label="Business card back">
    <div class="brand">
      <span class="brand__mark"></span>
      <span class="brand__name">Ferro Labs</span>
      <span class="brand__tagline">3D Printers and 3D Print Filaments</span>
    </div>
  </section>

</main>
</body>
</html>
```